Sheep ranch business card design

We need a business card design for our farm. We do all things sheep. We run Babydoll southdown sheep and use their fiber and meat. In the spring the lambs are sold. We shear them for their wool to make dryer balls, roving, and yarn which we sell. We also lease the sheep out to organic vineyards in the winter time to help them convert their weeds and cover crops to manure so they don't have to use tractors and tillers to mow and compact soil. Fennick Ranch also breeds Kangals which are livestock guard dogs that live with and protect the sheep. We also run a small herd of jersey cows, chickens, and bees but the sheep enterprise is the focal point. I would like to see the design use more earth tones and natural colors and have the feel of a modern and hip farm. I would also like our attached fennick ranch image to be used. The font family is dalle for our logo. That font can be used or something to compliment it. The attached pictures can be used as well but they are not necessary. One fennick ranch upload is in psd and one is in jpeg. Thank You and we look forward to seeing your work.
Updates

So many great designs. Not looking for anything "western." Font, design, or otherwise.

Industry/Entity Type

Livestock

Contact Information for Business Card

Fennick Ranch
Corin Fennick
www.fennickranch-example.com
fennickranch@mailbox-example.com
phone: 555 310-7282

```html
<!DOCTYPE html>
<html lang="en">
<head>
<meta charset="utf-8">
<title>Fennick Ranch — Business Card</title>
<link rel="stylesheet" href="https://fonts.googleapis.com/css2?family=Cinzel:wght@400;500&display=swap">
<style>
  :root {
    --paper: #ffffff;
    --ink: #5a5a5a;
    --frame: #6b6b6b;
  }
  * { margin: 0; padding: 0; box-sizing: border-box; }
  html, body {
    width: 1200px;
    height: 702px;
    overflow: hidden;
    background: var(--paper);
  }
  .card {
    position: relative;
    width: 1200px;
    height: 702px;
    background: var(--paper);
    color: var(--ink);
    font-family: "Cinzel", "Trajan Pro", serif;
  }
  .card__frame {
    position: absolute;
    left: 71px;
    top: 70px;
    width: 1060px;
    height: 564px;
    border: 2px solid var(--frame);
  }
  .brand {
    position: absolute;
    left: 0;
    right: 0;
    top: 118px;
    display: flex;
    justify-content: center;
    align-items: center;
    gap: 26px;
  }
  .brand__mark {
    width: 26px;
    height: 26px;
    border-radius: 50%;
    background: var(--ink);
  }
  .brand__name {
    font-size: 78px;
    font-weight: 500;
    letter-spacing: 0.06em;
    line-height: 1;
    color: var(--ink);
  }
  .person {
    position: absolute;
    left: 0;
    right: 0;
    top: 384px;
    text-align: center;
    font-size: 46px;
    font-weight: 400;
    letter-spacing: 0.02em;
    line-height: 1;
  }
  .divider {
    position: absolute;
    left: 379px;
    top: 460px;
    width: 444px;
    height: 2px;
    background: var(--ink);
  }
  .contact {
    position: absolute;
    left: 0;
    right: 0;
    top: 492px;
    list-style: none;
    text-align: center;
    line-height: 1;
  }
  .contact__item {
    font-size: 27px;
    letter-spacing: 0.02em;
    margin-bottom: 13px;
  }
  .contact__item--phone { font-size: 32px; margin-bottom: 12px; }
  .contact__item--email, .contact__item--web { font-size: 25px; }
</style>
</head>
<body>
  <main class="card">
    <div class="card__frame"></div>

    <header class="brand">
      <span class="brand__mark" aria-hidden="true"></span>
      <h1 class="brand__name">FENNICK RANCH</h1>
    </header>

    <h2 class="person">Corin Fennick</h2>
    <div class="divider" aria-hidden="true"></div>

    <ul class="contact">
      <li class="contact__item contact__item--phone">555 310-7282</li>
      <li class="contact__item contact__item--email">FENNICKRANCH@MAILBOX-EXAMPLE.COM</li>
      <li class="contact__item contact__item--web">WWW.FENNICKRANCH-EXAMPLE.COM</li>
    </ul>
  </main>
</body>
</html>
```